Website Design for Freeze-Dried Food Manufacturing Company (Pet Food & Agri-Food)

We are looking for a high-level web designer to create a clean, modern, premium website design for Tarquel, a freeze-dried food manufacturing company operating in both the pet food and agri-food space.
This is not a basic website build β we are looking for a designer who understands brand positioning, layout, and user flow, not just visuals.
π― Project Objective
Design a website that:
Clearly communicates our capabilities and value proposition
Feels premium, credible, and product-driven
Guides users through a simple, intuitive journey
Clean and Crips
A critical requirement is clearly separating:
π Pet Food
π Agri-Food
These must feel like two distinct pathways within the same brand experience.
We have attached detailed documents outlining structure, layout, and messaging. These should be followed closely.
π What Success Looks Like
A high-impact homepage with strong visual hierarchy
Clear entry points into Pet Food and Agri-Food
Clean, intentional layout (not cluttered or template-like)
Thoughtful spacing, typography, and flow
A design that feels considered and elevated, not generic
π¨ Design Direction
We are aiming for a:
Minimal, premium aesthetic
Warm, natural color palette (creams, browns, muted tones)
Ingredient and product-focused visuals
Avoid:
Overly corporate / industrial styles
Generic SaaS-style layouts
Busy or over-designed interfaces
End Goal
A website that immediately communicates:
Who we are
What we do
Why weβre different
In a way that feels premium, clear, and easy to navigate.
Link to current website: https://tarquelfoods.example/
https://tarquelhealth.example/wp-admin/

```html
<!DOCTYPE html>
<html lang="en">
<head>
<meta charset="utf-8">
<title>Tarquel — Industrial Freeze-Drying &amp; Food Manufacturing</title>
<link href="https://fonts.googleapis.com/css2?family=Alegreya+Sans:wght@400;500&family=Roboto:wght@300;400;500;700&family=Noto+Serif:wght@400;500&family=Fira+Sans:wght@300;400&display=swap" rel="stylesheet">
<style>
:root{
  --brown:#8a4a1f;
  --brown-dark:#7a3f18;
  --cream:#f3e1d6;
  --cream-border:#e3c9b8;
  --green:#5f7046;
  --green-panel:#506352;
  --gold:#c7b27a;
  --ink:#3a3a3a;
  --muted:#555;
  --footer:#1b1816;
  --white:#fff;
}
*{box-sizing:border-box;margin:0;padding:0}
html,body{width:1200px;height:3206px;overflow:hidden}
body{position:relative;background:var(--white);font-family:"Roboto",sans-serif;color:var(--ink)}
/* header */
.site-header{position:absolute;left:0;top:0;width:1200px;height:68px;background:var(--white)}
.brand{position:absolute;left:160px;top:15px}
.brand-name{font-family:"Roboto",sans-serif;font-weight:400;font-size:28px;line-height:28px;color:var(--ink)}
.brand-tag{font-size:10px;color:#444;margin-top:1px}
.main-nav{position:absolute;left:386px;top:28px;display:flex;gap:14px;font-size:11.5px;color:#333;letter-spacing:.2px}
.main-nav span:nth-child(3){margin-right:6px}
.btn-header{position:absolute;left:931px;top:18px;width:108px;height:32px;border-radius:16px;background:var(--brown-dark);color:#fff;font-size:11px;display:flex;align-items:center;justify-content:center}
/* hero */
.hero{position:absolute;left:0;top:68px;width:1200px;height:572px;background:linear-gradient(180deg,#9c7243 0%,#b98a54 30%,#8f7548 52%,#7a6a3b 62%,#8a6a35 80%,#6f5428 100%)}
.hero-title{position:absolute;left:0;top:160px;width:1200px;text-align:center;font-family:"Alegreya Sans",sans-serif;font-weight:500;font-size:54px;line-height:55px;color:#fff}
.hero-sub{position:absolute;left:270px;top:280px;width:660px;text-align:center;font-size:16px;line-height:26px;color:#fff}
.btn-pill{position:absolute;display:flex;align-items:center;justify-content:center;gap:6px;border-radius:24px;font-weight:500;font-size:15px}
.hero .btn-pill{left:517px;top:357px;width:172px;height:47px;background:#fff;color:var(--brown)}
/* pathways */
.rule{position:absolute;left:28px;top:783px;width:1146px;height:1px;background:#eee}
.path-card{position:absolute;top:702px;width:423px;height:469px;background:var(--cream);border:1px solid var(--cream-border)}
.path-photo{position:absolute;left:0;top:0;width:100%;height:263px}
.path-icon{position:absolute;left:186px;top:237px;width:50px;height:46px;background:#fff;border-radius:8px;display:flex;align-items:center;justify-content:center;box-shadow:0 2px 6px rgba(0,0,0,.1)}
.path-title{position:absolute;left:0;top:298px;width:100%;text-align:center;font-size:23px;font-weight:400;color:var(--brown)}
.path-text{position:absolute;left:20px;top:338px;width:383px;text-align:center;font-size:13px;line-height:21px;color:#444}
.btn-outline{position:absolute;left:136px;top:394px;width:149px;height:34px;border:1px solid var(--brown);color:var(--brown);font-size:10px;font-weight:500;display:flex;align-items:center;justify-content:center;letter-spacing:.3px}
/* production band */
.production{position:absolute;left:0;top:1242px;width:1200px;height:336px;background:linear-gradient(180deg,#5d6d44,#64744a 60%,#5a6a40)}
.production h2{position:absolute;left:0;top:54px;width:1200px;text-align:center;font-family:"Fira Sans",sans-serif;font-weight:300;font-size:42px;line-height:44px;color:#fff}
.production p{position:absolute;left:330px;top:155px;width:540px;text-align:center;font-size:13px;line-height:23px;color:#fff}
.production .btn-pill{left:512px;top:226px;width:170px;height:44px;background:var(--gold);color:#5b5230}
/* capabilities */
.cap-title{position:absolute;left:0;top:1642px;width:1200px;text-align:center;font-family:"Fira Sans",sans-serif;font-weight:300;font-size:32px;color:#444}
.cap-item{position:absolute;top:1734px;width:200px;text-align:center}
.cap-icon{margin:0 auto;width:75px;height:67px;background:var(--cream);border:1px solid var(--cream-border);border-radius:4px;display:flex;align-items:center;justify-content:center}
.cap-item h3{margin-top:27px;font-size:14.5px;font-weight:400;color:#333}
.cap-item p{margin-top:8px;font-size:12px;line-height:21px;color:#444}
/* applications */
.apps-heading{position:absolute;left:162px;top:1983px;height:33px;border-left:3px solid var(--brown);padding-left:19px;font-family:"Noto Serif",serif;font-weight:400;font-size:28px;line-height:33px;color:#222}
.app-card{position:absolute;left:162px;width:426px;height:109px;background:#faf8f6;border:1px solid #ddd}
.app-thumb{position:absolute;left:18px;top:18px;width:72px;height:72px}
.app-card h3{position:absolute;left:108px;top:20px;font-family:"Noto Serif",serif;font-weight:400;font-size:21px;color:#222}
.app-card p{position:absolute;left:108px;top:54px;width:290px;font-size:11.5px;line-height:18px;color:#555}
/* why */
.why{position:absolute;left:626px;top:1983px;width:413px;height:463px;background:var(--green-panel);border-radius:4px;color:#fff}
.why h2{position:absolute;left:48px;top:40px;font-family:"Fira Sans",sans-serif;font-weight:400;font-size:27px}
.why-item{position:absolute;left:48px;width:340px}
.why-item h3{font-weight:400;font-size:17.5px;padding-left:27px;position:relative}
.why-item h3 svg{position:absolute;left:0;top:3px}
.why-item p{padding-left:27px;margin-top:9px;font-size:12px;line-height:21px;color:#eef}
/* cta */
.cta{position:absolute;left:0;top:2530px;width:1200px;height:296px;background:linear-gradient(135deg,#b0772f 0%,#c48c3e 40%,#a97028 70%,#8d5c22 100%)}
.cta h2{position:absolute;left:0;top:66px;width:1200px;text-align:center;font-family:"Alegreya Sans",sans-serif;font-weight:500;font-size:44px;color:#fff}
.cta p{position:absolute;left:170px;top:122px;width:860px;text-align:center;font-size:19px;line-height:29px;color:#fff}
.cta-btn{position:absolute;top:200px;height:36px;font-size:10.5px;display:flex;align-items:center;justify-content:center;letter-spacing:.3px}
.cta-solid{left:444px;width:150px;background:#fff;color:var(--brown)}
.cta-line{left:613px;width:167px;border:1.5px solid #fff;color:#fff}
/* footer */
.site-footer{position:absolute;left:0;top:2826px;width:1200px;height:380px;background:var(--footer);color:#ddd}
.foot-brand{position:absolute;left:160px;top:84px}
.foot-brand .name{font-weight:400;font-size:62px;line-height:58px;color:#eee}
.foot-brand .tag{font-size:20px;font-weight:300;color:#e8e1dc;margin-top:6px;line-height:24px}
.foot-about{position:absolute;left:161px;top:178px;width:260px;font-size:12.5px;line-height:21px;color:#ddd}
.foot-col-title{position:absolute;top:80px;font-size:16.5px;font-weight:500;color:#eee}
.foot-links{position:absolute;top:126px;font-size:11.5px;line-height:29px;color:#ddd;list-style:none}
.foot-links li::before{content:"›";margin-right:6px}
.contact-row{position:absolute;left:871px;font-size:11.5px;line-height:19px;color:#ddd;display:flex;gap:10px}
.foot-bar{position:absolute;left:0;top:300px;width:1200px;height:1px;background:#2d2926}
.copyright{position:absolute;left:160px;top:332px;font-size:13px;color:#ddd}
.social{position:absolute;left:893px;top:326px;display:flex;gap:8px}
.social span{width:28px;height:28px;border:1.5px solid #ddd;border-radius:50%}
</style>
</head>
<body>

<header class="site-header">
  <div class="brand"><div class="brand-name">Tarquel</div><div class="brand-tag">Freeze-Dried Food Makers</div></div>
  <nav class="main-nav"><span>HOME</span><span>ABOUT</span><span>APPLICATIONS</span><span>CAPABILITIES</span><span>QUALITY &amp; TRACEABILITY</span><span>WHY TARQUEL</span></nav>
  <div class="btn-header">CONTACT US</div>
</header>

<section class="hero" role="img" aria-label="Grain silos and a food processing plant beside a field at sunset">
  <h1 class="hero-title">Industrial Freeze-Drying &amp; Food<br>Manufacturing</h1>
  <p class="hero-sub">A fully integrated, closed-loop system from ingredient sourcing through to production, packaging, and distribution.</p>
  <div class="btn-pill"><svg width="18" height="13" viewBox="0 0 18 13" fill="none" stroke="currentColor" stroke-width="1.2"><rect x="1" y="1" width="16" height="11"/><path d="M1 1l8 6 8-6"/></svg>CONTACT US</div>
</section>

<div class="rule"></div>
<article class="path-card" style="left:168px">
  <div class="path-photo" role="img" aria-label="Dog sitting beside a bowl of dry pet food" style="background:linear-gradient(180deg,#cdbfa5,#c8a97a 55%,#b78a52)"></div>
  <div class="path-icon"><svg width="22" height="20" viewBox="0 0 22 20" fill="var(--brown)"><ellipse cx="5" cy="7" rx="2.2" ry="3"/><ellipse cx="9" cy="3.5" rx="2.2" ry="3"/><ellipse cx="14" cy="3.5" rx="2.2" ry="3"/><ellipse cx="18" cy="7" rx="2.2" ry="3"/><path d="M11.5 9c3 0 6 5 5 7.5-1 2-3 .5-5 .5s-4 1.5-5-.5c-1-2.5 2-7.5 5-7.5z"/></svg></div>
  <h2 class="path-title">Pet Food</h2>
  <p class="path-text">Freeze-dried meals, toppers, and treats designed for quality, consistency, and performance</p>
  <div class="btn-outline">EXPLORE PET FOOD</div>
</article>
<article class="path-card" style="left:609px">
  <div class="path-photo" role="img" aria-label="Baskets of fresh peaches and yellow fruit at a market stall" style="background:linear-gradient(135deg,#c7502c,#e9a23a 40%,#e6c23b 60%,#6b4a3a 85%)"></div>
  <div class="path-icon"><svg width="26" height="22" viewBox="0 0 26 22" fill="none" stroke="var(--brown)" stroke-width="1.2"><rect x="2" y="10" width="22" height="10"/><path d="M2 14h22M6 10c0-4 3-5 4-3M12 10c0-5 4-6 5-2M18 10c1-3 4-3 4 0"/></svg></div>
  <h2 class="path-title">Agri-Food</h2>
  <p class="path-text">Ingredient processing and preservation solutions<br>for food and agricultural applications.</p>
  <div class="btn-outline" style="left:133px">EXPLORE AGRI-FOOD</div>
</article>

<section class="production" role="img" aria-label="Green grass field background">
  <h2>Dedicated Production<br>Environments</h2>
  <p>Pet food and agri-food production are handled in separate, controlled environments to ensure product integrity, safety, and compliance across both categories.</p>
  <div class="btn-pill"><svg width="18" height="13" viewBox="0 0 18 13" fill="none" stroke="currentColor" stroke-width="1.2"><rect x="1" y="1" width="16" height="11"/><path d="M1 1l8 6 8-6"/></svg>CONTACT US</div>
</section>

<h2 class="cap-title">Our Capabilities</h2>
<div class="cap-item" style="left:149px">
  <div class="cap-icon"><svg width="40" height="40" viewBox="0 0 40 40" fill="none" stroke="var(--brown)" stroke-width="1.3"><path d="M20 6l12 14-12 14H12V20z"/><rect x="8" y="16" width="8" height="18" rx="1"/><circle cx="22" cy="14" r="1.5"/></svg></div>
  <h3>OEM / Private label</h3>
  <p>Custom product development tailored to your brand's unique standards.</p>
</div>
<div class="cap-item" style="left:383px">
  <div class="cap-icon"><svg width="40" height="40" viewBox="0 0 40 40" fill="none" stroke="var(--brown)" stroke-width="1.3"><rect x="8" y="14" width="22" height="18" rx="6"/><path d="M10 14c0-6 18-6 18 0M12 22h10"/><circle cx="29" cy="26" r="4"/></svg></div>
  <h3>Freeze Drying</h3>
  <p>Custom product development tailored to your brand's unique standards.</p>
</div>
<div class="cap-item" style="left:617px">
  <div class="cap-icon"><svg width="40" height="40" viewBox="0 0 40 40" fill="none" stroke="var(--brown)" stroke-width="1.3"><path d="M13 18a5 5 0 1 1 4-8 5 5 0 0 1 9 1 4 4 0 0 1 1 7H13z"/><path d="M10 34l20-14M30 34L10 20"/></svg></div>
  <h3>R&amp;D Test Kitchen</h3>
  <p>Custom product development tailored to your brand's unique standards.</p>
</div>
<div class="cap-item" style="left:853px">
  <div class="cap-icon"><svg width="40" height="40" viewBox="0 0 40 40" fill="none" stroke="var(--brown)" stroke-width="1.3"><ellipse cx="20" cy="9" rx="10" ry="3.5"/><path d="M10 9v22c0 2 4.5 3.5 10 3.5s10-1.5 10-3.5V9M10 16c0 2 4.5 3.5 10 3.5s10-1.5 10-3.5M10 23.5c0 2 4.5 3.5 10 3.5s10-1.5 10-3.5"/></svg></div>
  <h3>Storage &amp; Logistics</h3>
  <p>Custom product development tailored to your brand's unique standards.</p>
</div>

<h2 class="apps-heading">Applications</h2>
<div class="app-card" style="top:2055px">
  <div class="app-thumb" role="img" aria-label="Close-up of freeze-dried treat texture" style="background:linear-gradient(135deg,#222,#777 50%,#333)"></div>
  <h3>Freeze-dried treats</h3>
  <p>Single-ingredient &amp; functional formulations for healthy rewards.</p>
</div>
<div class="app-card" style="top:2183px">
  <div class="app-thumb" role="img" aria-label="Bowl of granular meal topper seen from above" style="background:radial-gradient(circle,#9a9a95 30%,#d8d8d4 70%)"></div>
  <h3>Toppers</h3>
  <p>Meal &amp; hydration toppers designed to enhance daily nutrition.</p>
</div>
<div class="app-card" style="top:2310px">
  <div class="app-thumb" role="img" aria-label="Supplement bottles and containers on a dark background" style="background:linear-gradient(180deg,#111,#555 60%,#bbb)"></div>
  <h3>Functional formats</h3>
  <p>Powders, pucks, &amp; custom blends for specialized dietary needs.</p>
</div>

<aside class="why">
  <h2>Why Tarquel</h2>
  <div class="why-item" style="top:97px"><h3><svg width="16" height="16" viewBox="0 0 16 16"><circle cx="8" cy="8" r="7.5" fill="#d9c8a4"/><path d="M4.5 8.2l2.3 2.3 4.5-4.6" stroke="var(--green-panel)" stroke-width="1.6" fill="none"/></svg>Human-grade ingredient focus</h3><p>We source only the highest quality materials suitable for human consumption.</p></div>
  <div class="why-item" style="top:182px"><h3><svg width="16" height="16" viewBox="0 0 16 16"><circle cx="8" cy="8" r="7.5" fill="#d9c8a4"/><path d="M4.5 8.2l2.3 2.3 4.5-4.6" stroke="var(--green-panel)" stroke-width="1.6" fill="none"/></svg>Scalable production</h3><p>Integrated manufacturing process ensuring total control from start to finish.</p></div>
  <div class="why-item" style="top:265px"><h3><svg width="16" height="16" viewBox="0 0 16 16"><circle cx="8" cy="8" r="7.5" fill="#d9c8a4"/><path d="M4.5 8.2l2.3 2.3 4.5-4.6" stroke="var(--green-panel)" stroke-width="1.6" fill="none"/></svg>Quality &amp; traceability</h3><p>Complete transparency across the entire supply chain and manufacturing cycle.</p></div>
  <div class="why-item" style="top:350px"><h3><svg width="16" height="16" viewBox="0 0 16 16"><circle cx="8" cy="8" r="7.5" fill="#d9c8a4"/><path d="M4.5 8.2l2.3 2.3 4.5-4.6" stroke="var(--green-panel)" stroke-width="1.6" fill="none"/></svg>Closed-loop system</h3><p>Reliable manufacturing capacity designed to grow alongside your brand.</p></div>
</aside>

<section class="cta" role="img" aria-label="Close-up of golden wheat stalks">
  <h2>Let's Build Something Together</h2>
  <p>Ready to bring your premium pet food or agri-food product to life with industry-leading freeze-dried expertise?</p>
  <div class="cta-btn cta-solid">START A PROJECT</div>
  <div class="cta-btn cta-line">CONTACT OUR TEAM</div>
</section>

<footer class="site-footer">
  <div class="foot-brand"><div class="name">Tarquel</div><div class="tag">Freeze-Dried Food Makers</div></div>
  <p class="foot-about">A fully integrated, closed-loop system from ingredient sourcing through to production, packaging, and distribution</p>
  <h3 class="foot-col-title" style="left:510px">QUICK LINKS</h3>
  <ul class="foot-links" style="left:510px"><li>Home</li><li>About</li><li>Applications</li><li>Capabilities</li></ul>
  <ul class="foot-links" style="left:654px"><li>Quality &amp; Traceability</li><li>Why Tarquel</li><li>Contact Us</li><li>Privacy Policy</li></ul>
  <h3 class="foot-col-title" style="left:871px">CONTACT INFO</h3>
  <div class="contact-row" style="top:124px"><svg width="14" height="16" viewBox="0 0 14 16" fill="none" stroke="#ccc"><path d="M7 15s5-5 5-9A5 5 0 0 0 2 6c0 4 5 9 5 9z"/><circle cx="7" cy="6" r="1.8"/></svg><span>Lorem Ipsum dummy text<br>the printing and &nbsp;industry.</span></div>
  <div class="contact-row" style="top:178px"><svg width="14" height="12" viewBox="0 0 14 12" fill="none" stroke="#ccc"><rect x=".5" y="1" width="13" height="10"/><path d="M.5 1l6.5 5 6.5-5"/></svg><span>support@tarquelfoods.example</span></div>
  <div class="contact-row" style="top:218px"><svg width="14" height="14" viewBox="0 0 14 14" fill="none" stroke="#ccc"><path d="M3 1l2 3-1.5 1.5a8 8 0 0 0 5 5L10 9l3 2-1 2C6 13 1 8 1 2z"/></svg><span>555.010.4477</span></div>
  <div class="foot-bar"></div>
  <p class="copyright">© 2026 tarquelfoods.example. All Rights Reserved</p>
  <div class="social"><span></span><span></span><span></span><span></span></div>
</footer>

</body>
</html>
```